Velmora Cosmetics & Designer Jewellery Business Card

I'm an Independent Distributor for Velmora Cosmetics (a direct sales company) which supplies Skin care, anti-ageing, makeup, body care, hair care, Fenwick Naturals, therapeutic, fragrance, sun care and mens skin care. Also supplying Velmora Designer Jewellery.

I'm looking for a classy, elegant business card design, something simple but fresh, with soft colours (nothing hot pink or floral). I like gold or silver embossing if that's possible.

Target Market(s)

All ages and genders but predominantly 25+ females

Industry/Entity Type

Hair

Contact Information for Business Card

Tobin Carlyle
Independent Distributor - Velmora Cosmetics & Velmora Designer Jewellery
Ph: 0483 259 470
Email: tobin@quorvel.org
Product Info & Online Orders: www.velmoracosmetics-example.com.au/tobincarlyle

Requirements
Must have
• Both the Velmora Cosmetics and Velmora Designer Jewellery logos - any suitable combination of the attached files. I also have the Velmora Cosmetics logos in mono if required.
Also must include: Distributor ID 384752

```html
<!DOCTYPE html>
<html lang="en">
<head>
<meta charset="utf-8">
<title>Velmora Cosmetics &amp; Designer Jewellery Business Card</title>
<link rel="stylesheet" href="https://fonts.googleapis.com/css2?family=Cinzel:wght@400;500&family=Lato:wght@300;400&display=swap">
<style>
  :root {
    --backdrop: #e9e6e1;
    --card: #0e0e0e;
    --card-edge: #1c1c1c;
    --gold: #b9975e;
    --gold-soft: #8f7548;
    --text-light: #d9d2c4;
    --shadow: rgba(0, 0, 0, 0.28);
  }
  * { box-sizing: border-box; margin: 0; padding: 0; }
  html, body {
    width: 900px;
    height: 1200px;
    overflow: hidden;
    background: var(--backdrop);
  }
  .canvas {
    position: relative;
    width: 900px;
    height: 1200px;
  }
  .card {
    position: absolute;
    left: 40px;
    width: 820px;
    height: 480px;
    background: var(--card);
    border: 1px solid var(--card-edge);
    box-shadow: 0 14px 34px var(--shadow);
    color: var(--gold);
    font-family: "Cinzel", serif;
  }
  .card--front { top: 80px; }
  .card--back { top: 640px; }

  .brand {
    position: absolute;
    display: flex;
    flex-direction: column;
    align-items: center;
    text-align: center;
  }
  .brand__dot {
    border-radius: 50%;
    background: var(--gold);
  }
  .brand__name,
  .brand__sub {
    font-family: "Cinzel", serif;
    font-weight: 400;
    color: var(--gold);
    letter-spacing: 0.04em;
    line-height: 1.1;
    white-space: nowrap;
  }
  .brand__role {
    font-family: "Lato", sans-serif;
    font-weight: 300;
    color: var(--gold-soft);
    letter-spacing: 0.03em;
    white-space: nowrap;
  }

  /* front */
  .card--front .brand--jewellery { left: 80px; top: 150px; width: 260px; }
  .card--front .brand--jewellery .brand__dot { width: 46px; height: 46px; margin-bottom: 16px; }
  .card--front .brand--jewellery .brand__name { font-size: 26px; }
  .card--front .brand--jewellery .brand__sub { font-size: 15px; letter-spacing: 0.02em; }
  .card--front .brand--jewellery .brand__role { font-size: 12px; margin-top: 6px; }

  .card--front .brand--cosmetics { left: 400px; top: 150px; width: 360px; }
  .card--front .brand--cosmetics .brand__dot { width: 40px; height: 40px; margin-bottom: 14px; }
  .card--front .brand--cosmetics .brand__name { font-size: 44px; }
  .card--front .brand--cosmetics .brand__sub { font-size: 26px; letter-spacing: 0.12em; }
  .card--front .brand--cosmetics .brand__role { font-size: 20px; margin-top: 6px; }

  /* back */
  .card--back .brand--jewellery { left: 70px; top: 60px; width: 240px; }
  .card--back .brand--cosmetics { left: 70px; top: 200px; width: 240px; }
  .card--back .brand__dot { width: 26px; height: 26px; margin-bottom: 10px; }
  .card--back .brand__name { font-size: 18px; }
  .card--back .brand__sub { font-size: 11px; letter-spacing: 0.02em; }
  .card--back .brand__role { font-size: 10px; margin-top: 5px; }

  .divider {
    position: absolute;
    left: 385px;
    top: 55px;
    width: 1px;
    height: 300px;
    background: var(--gold-soft);
  }

  .contact {
    position: absolute;
    left: 520px;
    top: 105px;
    width: 280px;
  }
  .contact__name {
    font-size: 30px;
    font-weight: 400;
    color: var(--text-light);
    letter-spacing: 0.03em;
    white-space: nowrap;
  }
  .contact__title {
    font-size: 12px;
    color: var(--gold);
    letter-spacing: 0.06em;
    margin-top: 4px;
  }
  .contact__id {
    font-family: "Lato", sans-serif;
    font-size: 12px;
    color: var(--gold-soft);
    letter-spacing: 0.04em;
    margin-top: 6px;
  }
  .contact__list {
    list-style: none;
    margin-top: 58px;
  }
  .contact__item {
    display: flex;
    align-items: center;
    gap: 12px;
    font-family: "Lato", sans-serif;
    font-size: 16px;
    color: var(--text-light);
    margin-bottom: 14px;
  }
  .contact__icon { width: 18px; height: 18px; flex: none; }

  .orders {
    position: absolute;
    left: 0;
    right: 0;
    bottom: 40px;
    text-align: center;
    font-size: 15px;
    color: var(--text-light);
    letter-spacing: 0.02em;
    white-space: nowrap;
  }
</style>
</head>
<body>
<main class="canvas">

  <section class="card card--front" aria-label="Business card front">
    <div class="brand brand--jewellery">
      <span class="brand__dot"></span>
      <span class="brand__name">Velmora</span>
      <span class="brand__sub">Designer Jewellery</span>
      <span class="brand__role">Independent distributor</span>
    </div>
    <div class="brand brand--cosmetics">
      <span class="brand__dot"></span>
      <span class="brand__name">Velmora</span>
      <span class="brand__sub">Cosmetics</span>
      <span class="brand__role">Independent distributor</span>
    </div>
  </section>

  <section class="card card--back" aria-label="Business card back">
    <div class="brand brand--jewellery">
      <span class="brand__dot"></span>
      <span class="brand__name">Velmora</span>
      <span class="brand__sub">Designer Jewellery</span>
      <span class="brand__role">Independent distributor</span>
    </div>
    <div class="brand brand--cosmetics">
      <span class="brand__dot"></span>
      <span class="brand__name">Velmora</span>
      <span class="brand__sub">Cosmetics</span>
      <span class="brand__role">Independent distributor</span>
    </div>

    <div class="divider"></div>

    <div class="contact">
      <h1 class="contact__name">Tobin Carlyle</h1>
      <p class="contact__title">Independent Distributor</p>
      <p class="contact__id">Distributor ID 384752</p>
      <ul class="contact__list">
        <li class="contact__item">
          <svg class="contact__icon" viewBox="0 0 24 24" aria-hidden="true">
            <circle cx="12" cy="12" r="11" fill="none" stroke="#b9975e" stroke-width="1.5"/>
            <path d="M8.5 7c.6 0 1.2 1.6 1.2 2.2 0 .6-.8.9-.8 1.4.4 1.4 2 3 3.4 3.4.5 0 .8-.8 1.4-.8.6 0 2.2.6 2.2 1.2 0 1-1 1.8-2 1.8-3.3 0-7.2-3.9-7.2-7.2 0-1 .8-2 1.8-2z" fill="#b9975e"/>
          </svg>
          <span>0483 259 470</span>
        </li>
        <li class="contact__item">
          <svg class="contact__icon" viewBox="0 0 24 24" aria-hidden="true">
            <circle cx="12" cy="12" r="11" fill="none" stroke="#b9975e" stroke-width="1.5"/>
            <rect x="6.5" y="8" width="11" height="8" rx="1" fill="none" stroke="#b9975e" stroke-width="1.3"/>
            <path d="M6.8 8.5 12 12.5l5.2-4" fill="none" stroke="#b9975e" stroke-width="1.3"/>
          </svg>
          <span>tobin@quorvel.org</span>
        </li>
      </ul>
    </div>

    <p class="orders">Product Info &amp; Online Orders: www.velmoracosmetics-example.com.au/tobincarlyle</p>
  </section>

</main>
</body>
</html>
```